Redesign our business card for more impact

We want to completely replace the back design of our card, and refresh or even change the front entirely. We are happy with our black Q7 logo and do not want to change it.
Our company address changed too. It is now 58 Corvallen, Brenmoor, NV 92741
Updates

It was reported by Sketch Harbor email today that the uploaded files didnt upload. I am trying again.

Target Market(s)

Architects and Building Owners (People making multi-million dollar decisions)

Industry/Entity Type

Consulting Engineering

Contact Information for Business Card

Contact info on the front. "wallpaper" design on back with tag line on the back "Engineering Your Future"

Font styles to use
Sans Serif

Requirements
Must have
• A vivid, modern, impactful ...but tasteful back of card design. It should communicate our premier status, but grab attention as innovative. DESIGN SHOULD BE ELEGANT AND NOT TOO BUSY.
Nice to have
• Repeating pattern, multi-color, something creative...
Should not have
• Anything that looks too playful or that we are not serious professionals. It should also not be too boring or conservative.

```html
<!DOCTYPE html>
<html lang="en">
<head>
<meta charset="utf-8">
<title>Q7 Engineering — Business Card</title>
<link rel="stylesheet" href="https://fonts.googleapis.com/css2?family=Inter:wght@400;500;700;800&display=swap">
<style>
  :root {
    --page-bg: #e8e8e7;
    --card-bg: #242422;
    --ink-light: #e9e6dc;
    --ink-muted: #8c8b84;
    --frame-line: #7d7c76;
    --pattern-blue: #3a7fc4;
    --pattern-cream: #e8e4d6;
    --label-ink: #2a2a2a;
  }
  * { margin: 0; padding: 0; box-sizing: border-box; }
  html, body {
    width: 1200px; height: 1200px; overflow: hidden;
    background: var(--page-bg);
    font-family: "Inter", sans-serif;
  }
  .canvas { position: relative; width: 1200px; height: 1200px; }

  .card {
    position: absolute; top: 152px;
    width: 472px; height: 868px;
    background: var(--card-bg);
    box-shadow: 0 3px 8px rgba(0,0,0,0.18);
    overflow: hidden;
  }
  .card--front { left: 98px; }
  .card--back { left: 630px; }

  .card-frame { position: absolute; inset: 0; width: 100%; height: 100%; }

  .brand-name {
    position: absolute; top: 126px; left: 0; width: 100%;
    text-align: center;
    font-size: 58px; font-weight: 800; line-height: 1;
    color: var(--ink-light);
    letter-spacing: -1px;
  }

  .person { position: absolute; top: 350px; left: 0; width: 100%; text-align: center; }
  .person-name { font-size: 37px; font-weight: 400; color: var(--ink-light); line-height: 1.2; }
  .person-title { font-size: 24px; font-weight: 400; color: var(--ink-light); opacity: .85; margin-top: 6px; }

  .contact {
    position: absolute; top: 503px; left: 0; width: 100%;
    text-align: center; font-size: 23px; line-height: 35px;
    color: var(--ink-light);
  }
  .contact-label { color: var(--ink-muted); }
  .contact-address { margin-top: 33px; line-height: 34px; }

  .back-pattern {
    position: absolute; top: 0; left: 0; width: 100%; height: 738px;
    background:
      radial-gradient(ellipse at 25% 20%, rgba(58,127,196,0.55), transparent 55%),
      radial-gradient(ellipse at 75% 55%, rgba(232,228,214,0.28), transparent 55%),
      radial-gradient(ellipse at 30% 80%, rgba(58,127,196,0.45), transparent 55%),
      var(--card-bg);
  }
  .tagline {
    position: absolute; top: 792px; left: 0; width: 100%;
    text-align: center; font-size: 23px; color: var(--ink-light);
  }

  .side-label {
    position: absolute; top: 1060px; width: 472px;
    text-align: center; font-size: 31px; font-weight: 400;
    color: var(--label-ink); letter-spacing: 0.5px;
  }
  .side-label--front { left: 98px; }
  .side-label--back { left: 630px; }
</style>
</head>
<body>
<main class="canvas">

  <section class="card card--front">
    <svg class="card-frame" viewBox="0 0 472 868" aria-hidden="true">
      <g stroke="var(--frame-line)" stroke-width="1.4" fill="none">
        <path d="M19 42 V20 H90"/>
        <path d="M453 42 V20 H382"/>
        <path d="M19 808 V848 H90"/>
        <path d="M453 808 V848 H382"/>
        <path d="M113 848 H359"/>
        <path d="M20 270 V598"/>
        <path d="M452 270 V598"/>
        <path d="M20 270h10M20 283h6M20 296h6M20 309h6M20 322h6M20 335h10M20 348h6M20 361h6M20 374h6M20 387h6M20 400h10M20 413h6M20 426h6M20 439h6M20 452h6M20 465h10M20 478h6M20 491h6M20 504h6M20 517h6M20 530h10M20 543h6M20 556h6M20 569h6M20 582h6M20 595h10"/>
        <path d="M452 270h-10M452 283h-6M452 296h-6M452 309h-6M452 322h-6M452 335h-10M452 348h-6M452 361h-6M452 374h-6M452 387h-6M452 400h-10M452 413h-6M452 426h-6M452 439h-6M452 452h-6M452 465h-10M452 478h-6M452 491h-6M452 504h-6M452 517h-6M452 530h-10M452 543h-6M452 556h-6M452 569h-6M452 582h-6M452 595h-10"/>
      </g>
    </svg>

    <div class="brand-name">Q7</div>

    <div class="person">
      <p class="person-name">Alan Mercer</p>
      <p class="person-title">Senior Engineer</p>
    </div>

    <div class="contact">
      <p><span class="contact-label">Phone:</span> (555) 555-0172</p>
      <p><span class="contact-label">Email:</span> amercer@q7eng.com</p>
      <p><span class="contact-label">Website:</span> q7eng.com</p>
      <p class="contact-address"><span class="contact-label">Address:</span> 58 Corvallen,<br>Brenmoor, NV 92741</p>
    </div>
  </section>

  <section class="card card--back">
    <div class="back-pattern" role="img" aria-label="Flowing contour-line wallpaper pattern in blue and cream on black"></div>
    <p class="tagline">“Engineering Your Future”</p>
  </section>

  <p class="side-label side-label--front">FRONT</p>
  <p class="side-label side-label--back">BACK</p>

</main>
</body>
</html>
```